Brightvale Wound Care
Business cards and letterhead
Professional
Gregory Tamsett
Chief Executive Officer
3470 P Street NW
Suite 615
Washington, DC 20011
gtamsett@brightvale-wc.example
www.brightvale-wc.example
I need one that says "CEO" for the name above and one that says "Territory Manager". I also need (with the same design for the name Darren Pulcombe as "President" and one for him as well that says Senior Territory Manager"
I need to list these products on the back:
1. Verashu Negitive Pressure Wound Therapy
2. Brunix Negitive Pressure Wound Therapy
3. Orvil alternating pressure mattresses
Here is our logo please use this logo while doing our design for this project for both the business cards and letterhead. Thanks
Please add this one or the non-green one (also uploaded) some where on the card. Make it very small please.
Or add this one to the card somewhere. Whatever one looks better.

```html
<!DOCTYPE html>
<html lang="en">
<head>
<meta charset="utf-8">
<title>Brightvale Wound Care – Stationery</title>
<link rel="stylesheet" href="https://fonts.googleapis.com/css2?family=Ubuntu:wght@400;500;700&display=swap">
<style>
:root{
  --blue:#2b4fa0;
  --red:#e0202e;
  --ink:#444;
  --paper:#ffffff;
  --canvas:#ffffff;
  --edge:#d4d4d4;
}
*{box-sizing:border-box;margin:0;padding:0}
html,body{width:1200px;height:866px;overflow:hidden;background:var(--canvas)}
body{position:relative;font-family:"Ubuntu",Arial,sans-serif;color:var(--ink)}
.sheet{position:absolute;background:var(--paper);box-shadow:0 0 0 1px var(--edge),2px 2px 4px rgba(0,0,0,.15);overflow:hidden}
.sheet svg.bands{position:absolute;inset:0;width:100%;height:100%}
.brand{position:absolute;display:flex;align-items:center;gap:6px;color:var(--blue);font-weight:500;white-space:nowrap}
.brand .dot{border-radius:50%;background:var(--red);flex:none}

/* letterhead */
.letterhead{left:72px;top:72px;width:576px;height:468px}
.letterhead .brand{left:22px;top:26px;font-size:19px}
.letterhead .brand .dot{width:18px;height:18px}
.letterhead .address{position:absolute;right:24px;top:26px;text-align:right;color:#fff;font-size:11px;line-height:1.35;font-weight:500}

/* envelope */
.envelope{left:72px;top:552px;width:600px;height:204px}
.envelope .brand{left:18px;top:18px;font-size:17px}
.envelope .brand .dot{width:16px;height:16px}
.envelope .return{position:absolute;left:18px;bottom:20px;color:var(--red);font-size:10px}

/* business cards */
.card{width:240px;height:151px}
.card .brand{font-size:11px;gap:4px}
.card .brand .dot{width:10px;height:10px}
.card .person{position:absolute;text-align:center}
.card .name{color:var(--blue);font-size:11px;font-weight:500}
.card .role{color:var(--ink);font-size:5.5px;margin-top:1px}
.card .contact{position:absolute;font-size:4.6px;line-height:1.45;color:var(--ink)}
.card-front-a .brand{left:10px;top:12px}
.card-front-a .person{left:0;width:180px;top:44px}
.card-front-a .contact{left:12px;top:74px}
.card-front-b .mark{position:absolute;left:26px;top:34px;width:62px;height:62px;border-radius:50%;background:var(--blue)}
.card-front-b .person{left:110px;width:125px;top:16px}
.card-front-b .contact{left:112px;top:88px}
.card-1{left:667px;top:221px}
.card-2{left:919px;top:221px}
.card-3{left:667px;top:384px}
.card-4{left:919px;top:384px}

/* card back */
.card-back{left:823px;top:547px;width:240px;height:151px;background:linear-gradient(160deg,var(--red) 0%,#b02850 45%,var(--blue) 100%)}
.card-back .brand{left:42px;top:30px;color:#fff;font-size:11px;gap:4px}
.card-back .brand .dot{width:10px;height:10px;background:#fff}
.products{position:absolute;left:52px;top:72px;list-style:none;color:#fff;font-size:6.2px;line-height:1.6}
</style>
</head>
<body>

<section class="sheet letterhead" aria-label="Letterhead">
  <svg class="bands" viewBox="0 0 576 468" preserveAspectRatio="none" aria-hidden="true">
    <path d="M436 0H528V468H478C438 410 424 340 440 270C454 205 436 110 436 0Z" fill="var(--blue)"/>
    <path d="M530 0H560V468H496C522 420 532 360 532 300C532 220 530 120 530 0Z" fill="var(--red)"/>
  </svg>
  <div class="brand"><span class="dot"></span>Brightvale Wound Care</div>
  <div class="address">3470 P Street NW<br>Suite 615<br>Washington, DC 20011<br>Phone : 202-555-0148<br>Fax : 202-555-0173<br>www.brightvale-wc.example</div>
</section>

<section class="sheet envelope" aria-label="Envelope">
  <svg class="bands" viewBox="0 0 600 204" preserveAspectRatio="none" aria-hidden="true">
    <path d="M470 0H522V204H500C478 160 466 100 470 0Z" fill="var(--blue)"/>
    <path d="M524 0H548V204H512C526 160 526 90 524 0Z" fill="var(--red)"/>
  </svg>
  <div class="brand"><span class="dot"></span>Brightvale Wound Care</div>
  <div class="return">3470 P Street NW,Suite 615,Washington, DC 20011</div>
</section>

<section class="sheet card card-front-a card-1" aria-label="Business card front">
  <svg class="bands" viewBox="0 0 240 151" preserveAspectRatio="none" aria-hidden="true">
    <path d="M186 0H216V151H202C184 110 178 60 186 0Z" fill="var(--blue)"/>
    <path d="M218 0H240V151H208C220 110 222 60 218 0Z" fill="var(--red)"/>
  </svg>
  <div class="brand"><span class="dot"></span>Brightvale Wound Care</div>
  <div class="person"><p class="name">Darren Pulcombe</p><p class="role">CEO</p></div>
  <p class="contact">3470 P Street NW<br>Suite 615<br>Washington, DC 20011<br>Mobile : 202-555-0191<br>Phone : 202-555-0148<br>Fax : 202-555-0173<br>dpulcombe@brightvale-wc.example<br>www.brightvale-wc.example</p>
</section>

<section class="sheet card card-front-b card-2" aria-label="Business card front">
  <svg class="bands" viewBox="0 0 240 151" preserveAspectRatio="none" aria-hidden="true">
    <path d="M0 0H18C10 60 20 110 60 151H0Z" fill="var(--blue)"/>
    <path d="M0 108C20 132 46 146 84 151H0Z" fill="var(--red)"/>
  </svg>
  <span class="mark" aria-hidden="true"></span>
  <div class="person"><p class="name">Gregory Tamsett</p><p class="role">Territory Manager</p></div>
  <p class="contact">3470 P Street NW,Suite 615<br>Washington, DC 20011<br>Mobile : 202-555-0126<br>Phone : 202-555-0148<br>Email : gtamsett@brightvale-wc.example</p>
</section>

<section class="sheet card card-front-a card-3" aria-label="Business card front">
  <svg class="bands" viewBox="0 0 240 151" preserveAspectRatio="none" aria-hidden="true">
    <path d="M186 0H216V151H202C184 110 178 60 186 0Z" fill="var(--blue)"/>
    <path d="M218 0H240V151H208C220 110 222 60 218 0Z" fill="var(--red)"/>
  </svg>
  <div class="brand"><span class="dot"></span>Brightvale Wound Care</div>
  <div class="person"><p class="name">Darren Pulcombe</p><p class="role">President</p></div>
  <p class="contact">3470 P Street NW<br>Suite 615<br>Washington, DC 20011<br>Mobile : 202-555-0191<br>Phone : 202-555-0148<br>Fax : 202-555-0173<br>dpulcombe@brightvale-wc.example<br>www.brightvale-wc.example</p>
</section>

<section class="sheet card card-front-b card-4" aria-label="Business card front">
  <svg class="bands" viewBox="0 0 240 151" preserveAspectRatio="none" aria-hidden="true">
    <path d="M0 0H18C10 60 20 110 60 151H0Z" fill="var(--blue)"/>
    <path d="M0 108C20 132 46 146 84 151H0Z" fill="var(--red)"/>
  </svg>
  <span class="mark" aria-hidden="true"></span>
  <div class="person"><p class="name">Gregory Tamsett</p><p class="role">Chief Executive Officer</p></div>
  <p class="contact">3470 P Street NW,Suite 615<br>Washington, DC 20011<br>Mobile : 202-555-0126<br>Phone : 202-555-0148<br>Email : gtamsett@brightvale-wc.example</p>
</section>

<section class="sheet card-back" aria-label="Business card back">
  <div class="brand"><span class="dot"></span>Brightvale Wound Care</div>
  <ol class="products">
    <li>1. Verashu Negitive Pressure Wound Therapy</li>
    <li>2. Brunix Negitive Pressure Wound Therapy</li>
    <li>3. Orvil alternating pressure mattresses</li>
  </ol>
</section>

</body>
</html>
```